Willow Frost: CBD and Herbal Topical Pain product needs a brochure

We need a brochure that educates customers on the product. The product combines traditional Chinese herbs used for pain and swelling with a strong dose of CBD to apply topical with a glass, roll-on applicator. We would like to see dark blue as a dominant color or anything ice related. The logo is an iceberg but doesn't need to be included.

Target Market(s)

Cannabis Dispensaries, Chiro, Acu offices,
Health / Wellness, Alternative Medicine

Industry/Entity Type

Alternative Medicine

Colors
0455a3

Requirements
Must have
• Willow Frost
• 500mg CBD in 1oz
• For: Muscle, Joint Pain, Swelling, Acute Injuries, Chronic Pain, Arthritis
• Directions: Apply a thin layer of herbal formula over the affected area. Apply as needed.
• Caution: Avoid hot water shortly after application.
• Ingredients: Angelica Root, Camphor, Cannabidoil (CBD), Cinnamon, Dandelion, Gardenia, Ginger, Licorice, Menthol, Myrrh, Phellodendron Bark, Rhubarb, Safflower, Sesame Oil, Scutellaria
• Highlight amount of CBD: 500mg
• Secondary highlights it includes Turmeric and Magnesium
• Easy Roll-On Topical Pain Relief for Muscle Spasms, Joint Pain, Strains, Sprains, Swelling
• Increases circulation to increase recovery time. Great for athletes
• Stops pain by numbing painful, slower deep nerve signals by stimulating the faster, superficial nerves with a cooling sensation
• Reduce painful swelling and heat involved with inflammation.
• Breaks up damaged tissue to enhance the natural healing process
• Ingredients
• Dang Gui – Angelica : reduces swelling, generates tissue, alleviates pain, expels pus
• Cinnamon –Gui Zhi decreases arthritic pain
• Carthamus Flower / safflower –Hong Hua - reduces swelling, alleviates pain,
• Rhubarb – Da Huang -bruising, acute and chronic swelling
• Licorice –Gan Cao - alleviates spasms, anti-inflammatory
• Phellodendron Huang Bai– reduces swelling and pain
• Dandelion – Pu Gong Ying – reduces swelling and nodules, anti-inflammatory
• Mo Yao – Myrrh – reduces swelling, pain, bruising, and masses, promotes healing
• Ginger – Gan Jiang – chronic swelling, increases circulation
• Gardenia – Zhi Zi- Reduces swelling from trauma, bruising
• Scutellaria – Huang Qin – hot sores, swelling,
• Magnesium – helps muscle spasms
• Camphor – mild, local anesthetic effect, alleviates pain, pain and swelling from sprains
• Menthol – rashes, swelling, relaxes muscles
• Turmeric – reduces inflammation and swelling
• Sesame Oil – carrier oil
• Cannabidiol (CBD) Isolate
• Colloidal Silver (Natural Preservative)
• Formulated by a Herbalist and Doctor of Chinese Medicine, Dr. Dennis Harlow, DAOM
Nice to have
• Iceberg or ice theme
• Copy:
• Willow Frost blends traditional Chinese herbs with a potent dose of hemp derived cannabidiol (CBD) isolate. Instantly feel the cooling icy sensation penetrate deep into sore muscles and joints to sooth away pain.
• Not only does the menthol give a temporary cooling effect which helps numb pain, the other herbal ingredients continue to soothe tight, achy muscles and joints. It can also be applied for an acute sprain or strain to reduce swelling, just like applying ice.
• Ice is used by athletes and recommended by doctors to reduce pain and swelling. Willow Frost can reduce pain and swelling without having to carry a bag of ice around.
• With the easy roll-on application, you dont even have to get your hands cold!
• Traditional Chinese Medicine has used the same herbs for thousands of years to help ease the pain of injuries during battle. Herbal plasters, liniments, and oils were the most common application to maximize the healing benefits of the herbs. Willow Frost uses organic, raw herbs which are ground into a fine powder and further extracted in sesame oil. Once extracted, the oil is filtered and then CBD is then added as the oil is cooling.
• Pictures of a few of the herbs - I have a few already if needed

```html
<!DOCTYPE html>
<html lang="en">
<head>
<meta charset="utf-8">
<title>Willow Frost – Pain Relief Brochure</title>
<link href="https://fonts.googleapis.com/css2?family=Montserrat:wght@700;800&family=Open+Sans:ital,wght@0,400;0,600;0,700;1,400&family=Roboto+Condensed:wght@400;700&display=swap" rel="stylesheet">
<style>
  :root{
    --navy:#25266b;
    --navy-deep:#1b1c52;
    --ice:#5aa6e0;
    --ice-pale:#d4e9f9;
    --link:#3d4db5;
    --ink:#1e1e24;
    --grey:#8c8f99;
    --paper:#ffffff;
    --stage:#eeeff2;
  }
  *{box-sizing:border-box;margin:0;padding:0}
  html,body{width:1200px;height:1169px;overflow:hidden;background:var(--stage)}
  body{font-family:"Open Sans",Arial,sans-serif;color:var(--ink);position:relative}
  .spread{position:absolute;left:240px;width:720px;height:557px;background:var(--paper);box-shadow:0 1px 4px rgba(0,0,0,.18);overflow:hidden}
  .spread--inside{top:18px}
  .spread--outside{top:594px}
  .panel{position:absolute;top:0;height:100%;overflow:hidden}
  .panel--navy{background:linear-gradient(170deg,var(--navy-deep) 0%,var(--navy) 38%,#3d6fb8 70%,var(--ice-pale) 100%)}
  .panel--navy::before{content:"";position:absolute;left:0;right:0;top:0;height:22px;background:var(--navy-deep);border-bottom:1px solid rgba(255,255,255,.25)}
  .placeholder{position:absolute}

  /* inside spread */
  .story{position:absolute;left:23px;top:38px;width:196px;color:#dfe3f5;font-size:12.2px;line-height:1.17;font-weight:400}
  .story p{margin-bottom:11px}
  .product-bottle{left:120px;top:330px;width:100px;height:227px;background:linear-gradient(180deg,#b9bcc4 0 14%,#3a2a1e 14%,#1c1510 100%);border-radius:28px 28px 0 0}
  .roll-badge{position:absolute;left:-32px;top:316px;width:166px;height:166px;border-radius:50%;background:var(--grey);border:5px solid #6d7eb3;padding:24px 0 0 54px;font-family:"Roboto Condensed",sans-serif;font-weight:700;font-size:11px;line-height:1.36;color:#fff;z-index:2}
  .benefits{position:absolute;left:258px;top:38px;width:200px}
  .benefit{display:flex;gap:10px;margin-bottom:12px}
  .benefit svg{flex:0 0 38px}
  .benefit-text{font-family:"Roboto Condensed",sans-serif;font-weight:700;font-size:9.6px;line-height:1.32;color:#fff;padding-top:3px}
  .benefit-list{list-style:none}
  .benefit-list li{position:relative;padding-left:7px;margin-bottom:5px}
  .benefit-list li::before{content:"•";position:absolute;left:0}
  .ingredients{position:absolute;left:478px;top:0;width:242px;height:100%;padding:20px 10px 0 26px}
  .ingredients h2{font-size:13.5px;font-weight:700;color:var(--navy);margin-bottom:6px}
  .ingredient{font-size:8.2px;line-height:1.08;margin-bottom:3.4px}
  .ingredient b{display:block;font-weight:400;color:var(--link);text-decoration:underline}
  .credit{position:absolute;left:26px;right:14px;bottom:16px;border-top:1px solid #999;padding-top:7px;font-size:8.8px;font-style:italic;color:#555;line-height:1.25;text-align:center}

  /* outside spread */
  .herbs{left:110px;top:0;width:124px;height:58px;background:linear-gradient(135deg,#e9dcc4,#b98a55 55%,#6b3a22)}
  .intro{position:absolute;left:24px;top:64px;width:200px;font-size:12.3px;line-height:1.1;color:var(--ink)}
  .intro p{margin-bottom:7px}
  .intro .brand{font-weight:700;color:var(--navy);font-size:14px}
  .ice-box{position:absolute;left:24px;top:360px;width:194px;height:168px;border:1.5px solid var(--navy)}
  .ice-box p{position:absolute;left:98px;top:10px;width:94px;font-size:10.2px;font-weight:600;color:var(--navy);line-height:1.33}
  .ice-box p+p{top:92px}
  .cover{left:234px;width:486px}
  .cover-brand{position:absolute;left:82px;top:44px;display:flex;align-items:center;gap:8px;font-family:"Roboto Condensed",sans-serif;font-weight:700;font-size:19px;color:#fff}
  .cover-brand i{width:9px;height:9px;border-radius:50%;background:#fff;display:block}
  .title{position:absolute;left:262px;top:40px;font-family:"Montserrat",sans-serif;font-weight:800;color:#fff;font-size:49px;line-height:.92;letter-spacing:.5px}
  .subtitle{position:absolute;left:262px;top:148px;font-family:"Montserrat",sans-serif;font-weight:700;color:#fff;font-size:12.5px;line-height:1.25}
  .dose{position:absolute;left:376px;top:216px;width:80px;height:80px;border-radius:50%;background:var(--grey);border:4px solid var(--navy);display:flex;align-items:center;justify-content:center;text-align:center;font-family:"Montserrat",sans-serif;font-weight:800;color:var(--navy);font-size:12.5px;line-height:1.05;z-index:2}
</style>
</head>
<body>

<section class="spread spread--inside" aria-label="Brochure inside spread">
  <div class="panel panel--navy" style="left:0;width:478px">
    <div class="story">
      <p>Traditional Chinese Medicine has used the same herbs for thousands of years to help ease the pain of injuries during battle.</p>
      <p>Herbal plasters, liniments, and oils were the most common application to maximize the healing benefits of the herbs.</p>
      <p>Willow Frost uses organic, raw herbs which are ground into a fine powder and further extracted in sesame oil.</p>
      <p>Once extracted, the oil is filtered and then CBD is then added as the oil is cooling.</p>
    </div>

    <div class="roll-badge">With the<br>easy roll–on<br>application, you<br>dont even have<br>to get your<br>hands cold!</div>

    <div class="placeholder product-bottle" role="img" aria-label="Amber glass roll-on bottle with Willow Frost Pain Relief label"></div>
    <div class="placeholder" role="img" aria-label="Golden oil splash" style="left:238px;top:330px;width:240px;height:210px;background:radial-gradient(ellipse at 60% 55%,#e8c463 0%,#a57c1e 45%,rgba(120,90,20,0) 72%)"></div>

    <div class="benefits">
      <div class="benefit">
        <svg width="38" height="38" viewBox="0 0 38 38" aria-hidden="true"><circle cx="19" cy="19" r="18" fill="#fff"/><circle cx="19" cy="19" r="11" fill="none" stroke="#25266b" stroke-width="1.6"/><circle cx="19" cy="19" r="7" fill="none" stroke="#25266b" stroke-width="1.6"/><circle cx="19" cy="19" r="3" fill="none" stroke="#25266b" stroke-width="1.6"/></svg>
        <div class="benefit-text">For muscle, joint pain, swelling,<br>arthritis, acute injuries,<br>chronic pain.</div>
      </div>
      <div class="benefit">
        <svg width="38" height="38" viewBox="0 0 38 38" aria-hidden="true"><circle cx="19" cy="19" r="18" fill="#fff"/><path d="M9 12h9v15H9zM20 12h9v15h-9z" fill="none" stroke="#25266b" stroke-width="1.6"/><path d="M24.5 17v7" stroke="#25266b" stroke-width="2"/><circle cx="24.5" cy="14.5" r="1" fill="#25266b"/></svg>
        <div class="benefit-text">Apply a thin layer of herbal formula<br>over the affected area. Apply as<br>needed.</div>
      </div>
      <div class="benefit">
        <svg width="38" height="38" viewBox="0 0 38 38" aria-hidden="true"><circle cx="19" cy="19" r="18" fill="#fff"/><path d="M19 8L30 28H8z" fill="none" stroke="#25266b" stroke-width="1.8" stroke-linejoin="round"/><path d="M19 15v7" stroke="#25266b" stroke-width="2.2"/><circle cx="19" cy="25" r="1.3" fill="#25266b"/></svg>
        <div class="benefit-text">Avoid hot water shortly after<br>application.</div>
      </div>
      <div class="benefit">
        <svg width="38" height="38" viewBox="0 0 38 38" aria-hidden="true"><circle cx="19" cy="19" r="18" fill="#fff"/><path d="M10 10v18h18" fill="none" stroke="#25266b" stroke-width="1.6"/><path d="M12 24l5-6 4 3 6-8" fill="none" stroke="#25266b" stroke-width="1.6"/></svg>
        <ul class="benefit-text benefit-list">
          <li>Increases circulation<br>to increase recovery time</li>
          <li>Great for athletes</li>
          <li>Stops pain by numbing painful, slower deep nerve signals by stimulating the faster, superficial nerves with a cooling sensation</li>
          <li>Reduce painful swelling and heat involved with inflammation</li>
          <li>Breaks up damaged tissue to enhance the natural healing process</li>
        </ul>
      </div>
    </div>
  </div>

  <div class="ingredients">
    <h2>Ingredients</h2>
    <div class="ingredient"><b>Dang Gui – Angelica</b>Reduces swelling, generates tissue, alleviates pain, expels pus.</div>
    <div class="ingredient"><b>Cinnamon – Gui Zhi</b>Decreases arthritic pain.</div>
    <div class="ingredient"><b>Carthamus Flower/safflower – Hong Hua</b>Bruising, acute and chronic swelling.</div>
    <div class="ingredient"><b>Rhubarb – Da Huang</b>Bruising, acute and chronic swelling.</div>
    <div class="ingredient"><b>Licorice –Gan Cao</b>Alleviates spasms, anti-inflammatory.</div>
    <div class="ingredient"><b>Phellodendron Huang Bai</b>Reduces swelling and pain.</div>
    <div class="ingredient"><b>Dandelion – Pu Gong Ying</b>Reduces swelling and nodules, anti-inflammatory</div>
    <div class="ingredient"><b>Mo Yao – Myrrh</b>Reduces swelling, pain, bruising, and masses, promotes healing.</div>
    <div class="ingredient"><b>Ginger – Gan Jiang</b>Chronic swelling, increases circulation.</div>
    <div class="ingredient"><b>Gardenia – Zhi Zi</b>Reduces swelling from trauma, bruising.</div>
    <div class="ingredient"><b>Scutellaria – Huang Qin</b>Hot sores, swelling.</div>
    <div class="ingredient"><b>Magnesium</b>Helps muscle spasms.</div>
    <div class="ingredient"><b>Camphor</b>Mild, local anesthetic effect, alleviates pain and swelling from sprains.</div>
    <div class="ingredient"><b>Menthol</b>Rashes, swelling, relaxes muscles.</div>
    <div class="ingredient"><b>Turmeric</b>Reduces inflammation and swelling.</div>
    <div class="ingredient"><b>Sesame Oil</b>Carrier oil.</div>
    <div class="ingredient"><b>Cannabidiol (CBD)</b>Isolate.</div>
    <div class="ingredient"><b>Colloidal Silver</b>Natural preservative.</div>
    <p class="credit">Formulated by a Herbalist and Doctor of<br>Chinese Medicine, Dr. Dennis Harlow, DAOM</p>
  </div>
</section>

<section class="spread spread--outside" aria-label="Brochure outside spread">
  <div class="placeholder herbs" role="img" aria-label="Dried Chinese herbs in bowls and on a wooden spoon"></div>

  <div class="intro">
    <p><span class="brand">Willow Frost</span><br>blends traditional Chinese herbs with a potent dose of hemp derived cannabidiol (CBD) isolate.</p>
    <p>Instantly feel the <b>cooling icy sensation</b> penetrate deep into sore muscles and joints to <b>sooth away pain</b>.</p>
    <p>Not only does the menthol give a temporary cooling effect which helps numb pain, the other herbal ingredients continue to soothe tight, achy muscles and joints.</p>
    <p>It can also be applied for an acute sprain or strain to reduce swelling, just like applying ice.</p>
  </div>

  <div class="ice-box">
    <div class="placeholder" role="img" aria-label="Hand holding a blue ice pack against a knee" style="left:0;top:0;width:92px;height:100%;background:linear-gradient(160deg,#f1d8c6,#d9b29a 50%,#6fb8e6 80%)"></div>
    <p>Ice is used by athletes and recommended by doctors to reduce pain and swelling.</p>
    <p>Willow Frost can reduce pain and swelling without having to carry a bag of ice around.</p>
  </div>

  <div class="panel panel--navy cover">
    <div class="cover-brand"><i></i>Willow Frost</div>
    <h1 class="title">PAIN<br>RELIEF</h1>
    <p class="subtitle">Menthol, CBD,<br>Turmeric &amp; Magnesium</p>
    <div class="dose">500mg<br>CBD<br>in 1oz</div>
    <div class="placeholder" role="img" aria-label="Amber glass roll-on bottle with Willow Frost Pain Relief label" style="left:255px;top:225px;width:110px;height:215px;background:linear-gradient(180deg,#b9bcc4 0 15%,#3a2a1e 15%,#1c1510 100%);border-radius:26px 26px 0 0"></div>
    <div class="placeholder" role="img" aria-label="Wooden mortar and pestle" style="left:360px;top:300px;width:126px;height:190px;background:linear-gradient(90deg,#6b4a2a,#b8875a 50%,#5a3b20)"></div>
    <div class="placeholder" role="img" aria-label="Turmeric powder and a hemp leaf" style="left:300px;top:420px;width:130px;height:100px;background:radial-gradient(ellipse at 50% 50%,#e8b526 0%,#7c9a3a 55%,rgba(124,154,58,0) 75%)"></div>
  </div>
</section>

</body>
</html>
```